Bed and Breakfast WebSite Design

We need a webdesign for a bed and breakfast in Germany. This house is located at the scenic river Mosel in Germany, a very small town called Piesport. It's a region known for its wines. A lot of nature, bicycle routes, hiking, boat tours...

The house itself is a former monastery and because of that a listed, historic buildung.
The house is entirely renewed and has a very modern, individual interieur with "boutique hotel" style rooms. Every room is different. Its family owned and operated.

The website should find a bridge between historic charme and modern individual friendlyness. Very straight, not fancy. The website should express familiy friendlyness, modern comfort and emphasize that its place to RELAX.

In the attachment you'll find a lot of photos of house and surrounding. Theres a separate zip with lumetra stockphotos of that particular location/town (not purchased yet).

Number of Pages Required

1 page

Requirements
Must have
• Should be "easily" made responsive.

```html
<!DOCTYPE html>
<html lang="de">
<head>
<meta charset="utf-8">
<title>Rebenhaus Ufertal – Bed &amp; Breakfast an der Mosel</title>
<link rel="stylesheet" href="https://fonts.googleapis.com/css2?family=Oswald:wght@300;400;500;600&family=Poppins:wght@400;500;600&display=swap">
<style>
:root{
  --green:#6f9a39;
  --green-dark:#5d8530;
  --nav-bg:#dfe8cc;
  --light:#f4f5f7;
  --ink:#1d1d1d;
  --text:#333;
  --muted:#555;
  --footer:#1f1f1f;
  --white:#fff;
  --star:#e8b21c;
}
*{margin:0;padding:0;box-sizing:border-box}
html,body{width:1200px;height:4835px;overflow:hidden}
body{font-family:"Poppins",sans-serif;color:var(--text);background:var(--white);position:relative}
.abs{position:absolute}
.container{position:absolute;left:111px;width:978px}
h2{font-family:"Oswald",sans-serif;font-weight:500;color:var(--ink);text-transform:uppercase;font-size:40px;letter-spacing:.3px;line-height:1.15}
.section-title{text-align:center;width:100%}
.btn{display:inline-block;background:var(--green);color:var(--white);font-size:13px;font-weight:600;text-transform:uppercase;padding:0 24px;height:36px;line-height:36px;border-radius:3px;letter-spacing:.3px}

/* top bar */
.topbar{top:0;left:0;width:1200px;height:41px;background:var(--green);color:var(--white);font-size:14px}
.topbar .contact{position:absolute;left:418px;top:11px;display:flex;gap:28px}
.topbar .contact span{display:flex;align-items:center;gap:5px}
.topbar .social{position:absolute;left:943px;top:7px;display:flex;gap:9px}
.topbar .social i{width:27px;height:27px;border-radius:50%;background:rgba(255,255,255,.25);display:block}

/* nav */
.nav{top:41px;left:0;width:1200px;height:72px;background:var(--nav-bg)}
.brand{position:absolute;left:111px;top:18px;font-family:"Oswald",sans-serif;font-weight:600;font-size:31px;color:var(--green);text-transform:uppercase;letter-spacing:.3px}
.menu{position:absolute;left:486px;top:28px;display:flex;gap:25px;font-size:14px;font-weight:500;color:var(--ink);text-transform:uppercase}
.nav .btn{position:absolute;left:942px;top:17px;height:39px;line-height:39px;font-size:14px;font-weight:500;padding:0 18px}

/* hero */
.hero{top:113px;left:0;width:1200px;height:629px;background:linear-gradient(180deg,#7d9bc4 0%,#b9c8d8 30%,#6a8a4a 58%,#3f6b2a 80%,#2f5422 100%)}
.hero h1{position:absolute;top:182px;width:100%;text-align:center;font-family:"Oswald",sans-serif;font-weight:500;font-size:54px;color:var(--white);text-transform:uppercase;letter-spacing:.5px}
.search{position:absolute;left:218px;top:268px;width:762px;height:53px;background:var(--white);display:flex;align-items:center;font-size:11px;color:var(--ink)}
.search .field{padding-left:22px;line-height:1.5}
.search .field small{display:block;font-size:9px;text-transform:uppercase}
.search .field em{font-style:normal;font-size:12px}
.search .go{position:absolute;right:4px;top:4px;width:150px;height:45px;background:var(--green);color:var(--white);font-size:18px;font-weight:500;display:flex;align-items:center;justify-content:center;gap:8px;text-transform:uppercase}
.dots{position:absolute;left:1120px;top:275px;display:flex;flex-direction:column;gap:12px}
.dots i{width:12px;height:12px;border-radius:50%;border:2px solid var(--white);display:block}
.dots i.on{background:var(--white)}

/* welcome */
.welcome{top:742px;left:0;width:1200px;height:616px;background:var(--light)}
.framed{position:absolute;background:var(--white);padding:8px;box-shadow:0 2px 10px rgba(0,0,0,.12)}
.framed .photo{width:100%;height:100%}
.copy{position:absolute;left:648px;width:441px;font-size:14px;line-height:28px;text-align:justify;color:var(--text)}
.copy h2{text-align:left;font-size:40px;margin-bottom:18px;line-height:1.18}
.copy h2 .thin{font-weight:300;display:block}
.copy p{margin-bottom:8px}
.copy .btn{margin-top:10px}

/* rooms */
.rooms{top:1358px;left:0;width:1200px;height:601px;background:var(--white)}
.lead{text-align:center;font-size:14px;line-height:28px;margin:14px auto 0;width:730px}
.room-grid{position:absolute;top:132px;left:0;display:flex;gap:18px}
.room{width:314px}
.room .photo{height:249px}
.room .label{height:52px;background:var(--green);color:var(--white);font-size:18px;font-weight:500;text-align:center;line-height:52px}

/* amenities */
.amenities{top:1959px;left:0;width:1200px;height:618px;background:var(--light)}

/* gallery */
.gallery{top:2577px;left:0;width:1200px;height:747px;background:var(--white)}
.gallery-grid{position:absolute;top:73px;left:0;display:grid;grid-template-columns:repeat(3,314px);grid-auto-rows:249px;gap:18px}

/* testimonials */
.testimonials{top:3324px;left:0;width:1200px;height:635px;background:var(--white)}
.quotes{position:absolute;top:84px;left:0;display:flex;gap:20px}
.quote{width:314px;height:411px;background:var(--white);border:1px solid #e6e6e6;border-radius:6px;box-shadow:0 2px 8px rgba(0,0,0,.05);text-align:center;position:relative}
.quote .avatar{width:126px;height:126px;border-radius:50%;margin:43px auto 0;background:linear-gradient(180deg,#cfd3d8,#8f9aa5)}
.quote h3{font-size:23px;font-weight:500;color:var(--ink);margin-top:30px}
.stars{display:flex;justify-content:center;gap:2px;margin-top:4px}
.quote p{font-size:15px;line-height:29px;margin:10px 24px 0;color:var(--text)}
.quote .rule{position:absolute;right:-30px;width:70px;border-top:1px dotted #bbb}

/* map */
.map{top:3959px;left:0;width:1200px;height:516px;background:linear-gradient(160deg,#eceae4,#e2e6df 60%,#d9dcd4)}
.map-card{position:absolute;left:592px;top:79px;width:248px;height:306px;background:var(--white);border-radius:4px;padding:10px;box-shadow:0 2px 8px rgba(0,0,0,.2);text-align:center;font-size:14px;font-weight:500;color:var(--ink);line-height:22px}
.map-card .photo{height:190px;margin-bottom:14px}
.map-card .tel{margin-top:14px}
.map-pin{position:absolute;left:858px;top:185px}

/* footer */
.footer{top:4475px;left:0;width:1200px;height:360px;background:var(--footer);color:var(--white)}
.footer h4{font-size:15px;font-weight:500;text-transform:uppercase;margin-bottom:18px}
.f-col{position:absolute;top:92px}
.f-brand{font-family:"Oswald",sans-serif;font-size:24px;font-weight:500;text-transform:uppercase;margin-top:-8px;margin-bottom:6px}
.f-col p,.f-col li{font-size:12px;line-height:21px}
.f-col ul{list-style:none}
.f-col li{line-height:28px;font-size:13px}
.f-social{display:flex;gap:8px;margin-top:22px}
.f-social i{width:30px;height:30px;border-radius:50%;background:var(--white);display:block}
.f-contact li{display:flex;align-items:flex-start;gap:10px;margin-bottom:10px;line-height:22px}
.f-contact .ico{width:26px;height:26px;border-radius:50%;background:var(--green);flex:none;display:flex;align-items:center;justify-content:center}
.subscribe{margin-top:14px;width:262px;height:46px;border-radius:23px;background:var(--white);position:relative;color:#777;font-size:13px;line-height:46px;padding-left:18px}
.subscribe .send{position:absolute;right:4px;top:4px;width:38px;height:38px;border-radius:50%;background:var(--green);display:flex;align-items:center;justify-content:center}
.footer .divider{position:absolute;left:111px;top:301px;width:978px;border-top:1px solid #444}
.footer .copyright{position:absolute;top:322px;width:100%;text-align:center;font-size:13px}
</style>
</head>
<body>

<header class="abs topbar">
  <div class="contact">
    <span><svg width="13" height="13" viewBox="0 0 24 24" fill="#fff"><path d="M6.6 10.8a15 15 0 006.6 6.6l2.2-2.2a1 1 0 011-.25 11.4 11.4 0 003.6.57 1 1 0 011 1V20a1 1 0 01-1 1A17 17 0 013 4a1 1 0 011-1h3.5a1 1 0 011 1c0 1.25.2 2.45.57 3.57a1 1 0 01-.25 1z"/></svg>Tel. +49(0)6500 - 12 34 56</span>
    <span><svg width="14" height="12" viewBox="0 0 24 20" fill="#fff"><path d="M2 0h20a2 2 0 012 2v16a2 2 0 01-2 2H2a2 2 0 01-2-2V2a2 2 0 012-2zm10 9L2 3v2l10 6 10-6V3z"/></svg>Email: info@rebenhaus-ufertal.de</span>
  </div>
  <div class="social"><i></i><i></i><i></i><i></i></div>
</header>

<nav class="abs nav">
  <div class="brand">Rebenhaus Ufertal</div>
  <div class="menu"><span>Home</span><span>About</span><span>Rooms</span><span>Specials</span><span>Contact Us</span></div>
  <span class="btn">Check Online</span>
</nav>

<section class="abs hero" role="img" aria-label="Panoramic photo of vineyard slopes above a bend of the Mosel river with the village">
  <h1>Rebenhaus Ufertal</h1>
  <div class="search">
    <div class="field" style="width:155px"><small>Check-in</small><em>26-01-2021</em></div>
    <div class="field" style="width:170px"><small>Staying for</small><em>1 night &nbsp;&nbsp;&nbsp;&nbsp;&nbsp;⌄</em></div>
    <div class="field" style="width:82px"><small>Adults</small><em>2 &nbsp;&nbsp;&nbsp;⌄</em></div>
    <div class="field" style="width:93px"><small>Children</small><em>0 &nbsp;&nbsp;&nbsp;⌄</em></div>
    <div class="field" style="width:90px"><small>Infants</small><em>0 &nbsp;&nbsp;&nbsp;⌄</em></div>
    <div class="go"><svg width="17" height="17" viewBox="0 0 24 24" fill="none" stroke="#fff" stroke-width="3"><circle cx="10" cy="10" r="7"/><path d="M15 15l6 6"/></svg>Search</div>
  </div>
  <div class="dots"><i class="on"></i><i></i><i></i><i></i></div>
</section>

<section class="abs welcome">
  <div class="framed" style="left:107px;top:75px;width:470px;height:470px">
    <div class="photo" role="img" aria-label="Photo of the half-timbered house by the river with trees and green bank" style="background:linear-gradient(180deg,#9bc0e6 0%,#dfe3e6 35%,#5d7a3c 65%,#2f4a28 100%)"></div>
  </div>
  <div class="copy" style="top:106px">
    <h2><span class="thin">Welcome to</span>Rebenhaus Ufertal</h2>
    <p>Rebenhaus genießen am Fluss Herzlich willkommen im Rebenhaus in Ufertal! Fühlen Sie sich zu Hause und genießen Sie die private Atmosphäre unseres Hauses, den Garten, den Blick auf die Weinberge und die Mosel!</p>
    <p>Gastfreundlichkeit hat in unserer Familie eine lange Tradition, die wir gerne fortführen. Unser Haus ist denkmalgeschützer Teil eines alten Kartäuserklosters und dies wollen wir weiter erhalten und beleben.</p>
    <span class="btn">Learn More</span>
  </div>
</section>

<section class="abs rooms">
  <div class="container" style="top:80px">
    <h2 class="section-title">Room &amp; Suites</h2>
    <p class="lead">Lorem ipsum dolor sit amet, consectetur adipiscing elit, sed do eiusmod tempor incididunt ut labore et dolore magna aliqua. Quis ipsum suspendisse ultrices gravida.</p>
    <div class="room-grid">
      <div class="room"><div class="photo" role="img" aria-label="Photo of a double room with white bedding and a floral wallpaper" style="background:linear-gradient(180deg,#7d8f6c,#d9d4c8 60%,#eeeeee)"></div><div class="label">Luxurious Double Room</div></div>
      <div class="room"><div class="photo" role="img" aria-label="Photo of a double room with grey bedspread and wooden furniture" style="background:linear-gradient(180deg,#b9aa92,#6e6258 60%,#4a443f)"></div><div class="label">Luxurious Double Room</div></div>
      <div class="room"><div class="photo" role="img" aria-label="Photo of a bright double room with pink curtains and a striped blanket" style="background:linear-gradient(180deg,#e9d9d6,#c9b4ae 60%,#8a6c66)"></div><div class="label">Luxurious Double Room</div></div>
    </div>
  </div>
</section>

<section class="abs amenities">
  <div class="framed" style="left:107px;top:75px;width:470px;height:470px">
    <div class="photo" role="img" aria-label="Photo of the Mosel valley with vineyards, a small chapel and the river" style="background:linear-gradient(180deg,#7fa0c9 0%,#cfd7df 30%,#6f8a5a 55%,#4a6b34 100%)"></div>
  </div>
  <div class="copy" style="top:146px">
    <h2>Amenities &amp; &nbsp;Facilities</h2>
    <p>Bicycle routes, hiking, boat tours Direkt an der Mosel, nur getrennt durch den Radweg am Fuße der malerischen Weinberge des bekannten „Ufertaler Sonnenhang“, liegt unsere familiäre Pension „Rebenhaus“. Sieben neu renovierte, individuell eingerichtete Zimmer mit Bad (Sat-TV, WLAN) laden Sie ein mit Blick in das romantische Moseltal. Im alte Denkmalwürdigen Winzerhaus aus dem Jahre 1794 steht</p>
    <span class="btn">Learn More</span>
  </div>
</section>

<section class="abs gallery">
  <div class="container" style="top:84px">
    <h2 class="section-title">Our Gallery</h2>
    <div class="gallery-grid">
      <div role="img" aria-label="Photo of guests at a candlelit wine tasting in a vaulted cellar" style="background:linear-gradient(160deg,#3a2414,#7a4a22 50%,#2a1a10)"></div>
      <div role="img" aria-label="Photo of a long candlelit table set with wine glasses" style="background:linear-gradient(160deg,#2a1c16,#6a3a26 55%,#1f1612)"></div>
      <div role="img" aria-label="Photo of the garden gate with a carved wooden house sign" style="background:linear-gradient(180deg,#7fa8d8,#6a8a4a 50%,#5a4636)"></div>
      <div role="img" aria-label="Photo of a garden with a statue and a small gazebo" style="background:linear-gradient(180deg,#3e5a2c,#7a9a58 55%,#4a5e38)"></div>
      <div role="img" aria-label="Photo of a wicker beach chair lounger on the lawn" style="background:linear-gradient(180deg,#9aa38a,#7d8276 50%,#5f8a3c)"></div>
      <div role="img" aria-label="Photo of pallet lounge furniture with red cushions in the garden" style="background:linear-gradient(180deg,#6b8fb8,#5e7f42 45%,#8a8a82)"></div>
    </div>
  </div>
</section>

<section class="abs testimonials">
  <div class="container" style="top:70px">
    <h2 class="section-title">Client Testimonials</h2>
    <div class="quotes">
      <div class="quote">
        <div class="avatar" role="img" aria-label="Portrait photo of the guest"></div>
        <h3>Jonas Berger</h3>
        <div class="stars">
          <svg width="90" height="16" viewBox="0 0 90 16" fill="var(--star)"><g id="s"><path d="M8 0l2.4 5 5.4.6-4 3.7 1.1 5.4L8 12l-4.9 2.7 1.1-5.4-4-3.7L5.6 5z"/></g><use href="#s" x="18"/><use href="#s" x="36"/><use href="#s" x="54"/><use href="#s" x="72"/></svg>
        </div>
        <p>Lorem ipsum d amet, consectetur adipiscing elit, do eiusmod tempor incididunt ut lab et dolore magna aliqua. Quis ipsum</p>
        <span class="rule" style="top:33px"></span><span class="rule" style="top:376px"></span>
      </div>
      <div class="quote">
        <div class="avatar" role="img" aria-label="Portrait photo of the guest"></div>
        <h3>Jonas Berger</h3>
        <div class="stars"><svg width="90" height="16" viewBox="0 0 90 16" fill="var(--star)"><use href="#s"/><use href="#s" x="18"/><use href="#s" x="36"/><use href="#s" x="54"/><use href="#s" x="72"/></svg></div>
        <p>Lorem ipsum d amet, consectetur adipiscing elit, do eiusmod tempor incididunt ut lab et dolore magna aliqua. Quis ipsum</p>
        <span class="rule" style="top:33px"></span><span class="rule" style="top:376px"></span>
      </div>
      <div class="quote">
        <div class="avatar" role="img" aria-label="Portrait photo of the guest"></div>
        <h3>Jonas Berger</h3>
        <div class="stars"><svg width="90" height="16" viewBox="0 0 90 16" fill="var(--star)"><use href="#s"/><use href="#s" x="18"/><use href="#s" x="36"/><use href="#s" x="54"/><use href="#s" x="72"/></svg></div>
        <p>Lorem ipsum d amet, consectetur adipiscing elit, do eiusmod tempor incididunt ut lab et dolore magna aliqua. Quis ipsum</p>
      </div>
    </div>
  </div>
</section>

<section class="abs map" role="img" aria-label="Street map of the village along the Mosel showing the location of the house">
  <div class="map-card">
    <div class="photo" role="img" aria-label="Photo of the house front with trees" style="background:linear-gradient(180deg,#4f6e36,#d7d3cc 55%,#3e5a2c)"></div>
    <div>Weinbergstraße 12 • 54321<br>Ufertal/Mosel</div>
    <div class="tel">Tel. +49(0)6500 - 12 34 56</div>
  </div>
  <svg class="map-pin" width="26" height="36" viewBox="0 0 24 34"><path d="M12 0a12 12 0 0112 12c0 9-12 22-12 22S0 21 0 12A12 12 0 0112 0z" fill="#d9303a"/><circle cx="12" cy="12" r="4.5" fill="#fff"/></svg>
</section>

<footer class="abs footer">
  <div class="f-col" style="left:111px;width:230px">
    <div class="f-brand">Rebenhaus Ufertal</div>
    <p>Sed ut perspiciatis unde omis iste natus error sit voluptatem atium doloremque laudantium, totam rem</p>
    <div class="f-social"><i></i><i></i><i></i><i></i></div>
  </div>
  <div class="f-col" style="left:377px">
    <h4>Quick Links</h4>
    <ul style="margin-top:-6px"><li>Home</li><li>About</li><li>Rooms</li><li>Specials</li><li>Contact Us</li></ul>
  </div>
  <div class="f-col" style="left:546px;width:240px">
    <h4 style="margin-top:-10px">Contact Us</h4>
    <ul class="f-contact">
      <li><span class="ico"><svg width="10" height="14" viewBox="0 0 24 34"><path d="M12 0a12 12 0 0112 12c0 9-12 22-12 22S0 21 0 12A12 12 0 0112 0z" fill="#fff"/></svg></span>Weinbergstraße 12 • 54321 Ufertal/Mosel</li>
      <li><span class="ico"><svg width="12" height="12" viewBox="0 0 24 24" fill="#fff"><path d="M6.6 10.8a15 15 0 006.6 6.6l2.2-2.2a1 1 0 011-.25 11.4 11.4 0 003.6.57 1 1 0 011 1V20a1 1 0 01-1 1A17 17 0 013 4a1 1 0 011-1h3.5a1 1 0 011 1c0 1.25.2 2.45.57 3.57a1 1 0 01-.25 1z"/></svg></span>+49(0)6500 - 12 34 56</li>
      <li><span class="ico"><svg width="12" height="10" viewBox="0 0 24 20" fill="#fff"><path d="M2 0h20a2 2 0 012 2v16a2 2 0 01-2 2H2a2 2 0 01-2-2V2a2 2 0 012-2zm10 9L2 3v2l10 6 10-6V3z"/></svg></span>info@rebenhaus-ufertal.de</li>
    </ul>
  </div>
  <div class="f-col" style="left:826px;width:265px">
    <h4 style="margin-top:-10px">Subscribe to our blog</h4>
    <p style="font-size:13px;line-height:28px">Sign up today to get resources on how to attract and retain more customers!</p>
    <div class="subscribe">✉ Email Address<span class="send"><svg width="15" height="15" viewBox="0 0 24 24" fill="#fff"><path d="M2 21l21-9L2 3v7l15 2-15 2z"/></svg></span></div>
  </div>
  <div class="divider"></div>
  <div class="copyright">© 2022 Rebenhaus Ufertal. All Rights Reserved.</div>
</footer>

</body>
</html>
```